Postcard Design

We are a full service lawn maintenace and landscapig company. Everything from maintenance, fertilizer programs, to design and install.
I would like the card to have a classy look including our logo which is attached. The logo would just have to contain the lettering and the swooshes not the pine tree background if not needed.

```html
<!DOCTYPE html>
<html lang="en">
<head>
<meta charset="utf-8">
<title>Tall Cedar Landscaping – Postcard</title>
<link rel="stylesheet" href="https://fonts.googleapis.com/css2?family=Arimo:wght@400;500;700&family=Oswald:wght@500&display=swap">
<style>
  :root {
    --green-light: #9cbf52;
    --green: #85aa42;
    --green-dark: #6f9533;
    --sign-green: #7ea743;
    --white: #ffffff;
    --post: #d9dadb;
    --post-shade: #a9abad;
    --scene-top: #9fc9a0;
    --scene-bottom: #6aa83a;
    --text-shadow: rgba(40, 60, 10, 0.45);
  }
  html, body {
    margin: 0;
    padding: 0;
    overflow: hidden;
    background: var(--white);
  }
  .postcard {
    position: relative;
    width: 1200px;
    height: 863px;
    overflow: hidden;
    background: var(--white);
    font-family: "Arimo", Arial, sans-serif;
    color: var(--white);
  }
  .info-panel {
    position: absolute;
    left: 0;
    top: 0;
    width: 706px;
    height: 863px;
    background: radial-gradient(ellipse at 45% 45%, var(--green-light) 0%, var(--green) 55%, var(--green-dark) 100%);
  }
  .headline {
    position: absolute;
    left: 70px;
    top: 70px;
    margin: 0;
    font-size: 56px;
    font-weight: 500;
    line-height: 75px;
    white-space: nowrap;
    text-shadow: 2px 3px 4px var(--text-shadow);
  }
  .intro {
    position: absolute;
    left: 74px;
    top: 303px;
    margin: 0;
    font-size: 26px;
    line-height: 37.5px;
    white-space: nowrap;
    text-shadow: 1px 2px 3px var(--text-shadow);
  }
  .contact-lead,
  .contact-phone,
  .contact-email {
    position: absolute;
    left: 58px;
    width: 520px;
    margin: 0;
    text-align: center;
    white-space: nowrap;
    text-shadow: 1px 2px 3px var(--text-shadow);
  }
  .contact-lead {
    top: 503px;
    font-size: 26px;
    line-height: 34px;
  }
  .contact-phone {
    top: 543px;
    font-size: 70px;
    font-weight: 700;
    line-height: 76px;
  }
  .contact-email {
    top: 628px;
    font-size: 26px;
    line-height: 34px;
  }
  .contact-email strong { font-weight: 700; }
  .brand {
    position: absolute;
    left: 134px;
    top: 722px;
    display: flex;
    align-items: center;
    gap: 16px;
  }
  .brand-dot {
    width: 24px;
    height: 24px;
    border-radius: 50%;
    background: var(--white);
    flex: none;
  }
  .brand-name {
    font-size: 31px;
    font-weight: 400;
    line-height: 34px;
    letter-spacing: 2px;
    text-transform: uppercase;
    white-space: nowrap;
    color: var(--white);
  }
  .artwork {
    position: absolute;
    left: 0;
    top: 0;
  }
  .sign {
    position: absolute;
    left: 630px;
    top: 52px;
    width: 346px;
    height: 180px;
    background: var(--sign-green);
    border: 7px solid var(--white);
    outline: 6px solid var(--sign-green);
    box-sizing: border-box;
    transform: rotate(-4.5deg);
    display: flex;
    align-items: center;
    justify-content: center;
    box-shadow: 3px 5px 8px rgba(0,0,0,0.25);
  }
  .sign-text {
    font-family: "Oswald", "Arial Narrow", sans-serif;
    font-size: 90px;
    font-weight: 500;
    line-height: 1;
    letter-spacing: 1px;
    color: var(--white);
  }
</style>
</head>
<body>
<main class="postcard">
  <section class="info-panel">
    <h1 class="headline">Your key to<br>maintaining a<br>perfect lawn...</h1>
    <p class="intro">We are a full service lawn maintenace<br>and landscapeing company. We handle<br>everything from maintenance, fertilizer<br>programs, to design and installing.</p>
    <p class="contact-lead">For more information call</p>
    <p class="contact-phone">012 34 5678 9</p>
    <p class="contact-email">or email <strong>hello@tallcedar.com</strong></p>
    <div class="brand">
      <span class="brand-dot"></span>
      <span class="brand-name">Tall Cedar<br>Landscaping</span>
    </div>
  </section>

  <svg class="artwork" width="1200" height="863" viewBox="0 0 1200 863">
    <defs>
      <linearGradient id="post-tones" x1="0" y1="0" x2="1" y2="0">
        <stop offset="0" stop-color="var(--post-shade)"/>
        <stop offset="0.45" stop-color="var(--white)"/>
        <stop offset="1" stop-color="var(--post)"/>
      </linearGradient>
      <linearGradient id="scene-tones" x1="0" y1="0" x2="0" y2="1">
        <stop offset="0" stop-color="var(--scene-top)"/>
        <stop offset="1" stop-color="var(--scene-bottom)"/>
      </linearGradient>
    </defs>
    <rect class="sign-post" x="762" y="220" width="54" height="400" fill="url(#post-tones)"/>
    <rect class="keyhole-scene" role="img"
          aria-label="Illustration: garden scene seen through a keyhole, with a young tree, yellow flowers, a hedge, a red ride-on lawn mower and tall grass blades in front"
          x="715" y="272" width="425" height="560"
          fill="url(#scene-tones)"/>
  </svg>

  <div class="sign"><span class="sign-text">HIRE US!</span></div>
</main>
</body>
</html>
```